Harbor Nightclub

Nightclub flyer., digital single sided, for KV and PX. I included samples of some previous flyers we've used. Sample Info:
HARBOR
FRIDAYS
FRI MAY 1 2020
DJ VORTAN (club floor)
DJ RUZO & DJ TAV (residents on the lounge floor)
4217 Marlow Avenue Sacramento
www.harborvenuehall.example for list/VIP inquiries

Target Market(s)

Upscale top 40 crowd but want some cool and artsy like the examples included.

Font styles to use
Sans Serif

Requirements
Must have
• Harbor Logo
Nice to have
• Would be nice if the flyer can be incorporated later with DJ photos (sometimes we will add dj photos to pixagram etc). Would like a big city type of feel.
Should not have
• Nothing too sexual.

```html
<!DOCTYPE html>
<html lang="en">
<head>
<meta charset="utf-8">
<title>Harbor Fridays</title>
<link href="https://fonts.googleapis.com/css2?family=Roboto:wght@100;300;400;500&display=swap" rel="stylesheet">
<style>
  :root {
    --night: #07121a;
    --white: #f4f4f6;
    --orchid: #c98ad8;
    --neon-blue: #bfe6ff;
    --neon-pink: #f6a8f4;
    --photo-pink: rgba(200, 130, 180, 0.38);
    --photo-blue: rgba(150, 190, 230, 0.22);
  }
  * { margin: 0; padding: 0; box-sizing: border-box; }
  html, body { width: 960px; height: 1200px; overflow: hidden; background: var(--night); }
  .flyer {
    position: relative; width: 960px; height: 1200px; overflow: hidden;
    background: var(--night); color: var(--white);
    font-family: "Roboto", sans-serif;
  }
  .address {
    position: absolute; top: 32px; left: 0; width: 100%;
    text-align: center; font-weight: 300; font-size: 18px; letter-spacing: 12px;
    white-space: nowrap;
  }
  .photo-area {
    position: absolute; left: 0; top: 210px; width: 620px; height: 900px;
    background: radial-gradient(ellipse 60% 55% at 40% 50%, var(--photo-pink), var(--photo-blue) 55%, transparent 100%);
  }
  .neon-frames { position: absolute; left: 0; top: 0; }
  .neon-frames polygon { fill: none; stroke-width: 2.5; }
  .frame-blue { stroke: var(--neon-blue); filter: drop-shadow(0 0 5px #5fb8ff); }
  .frame-pink { stroke: var(--neon-pink); filter: drop-shadow(0 0 5px #e04ad8); }
  .lineup { position: absolute; right: 82px; text-align: right; white-space: nowrap; }
  .title {
    top: 140px; font-weight: 100; font-size: 140px; letter-spacing: 16px; line-height: 1;
    margin-right: -16px;
  }
  .date { top: 278px; font-weight: 300; font-size: 46px; letter-spacing: 6px; margin-right: -6px; }
  .floor-label {
    color: var(--orchid); font-weight: 500; font-size: 18px; letter-spacing: 8px; margin-right: -8px;
  }
  .floor-club { top: 416px; }
  .floor-lounge { top: 575px; }
  .dj { font-weight: 500; letter-spacing: 8px; margin-right: -8px; line-height: 1; }
  .dj-club { top: 462px; font-size: 50px; }
  .dj-lounge { top: 628px; font-size: 42px; line-height: 50px; }
  .website {
    position: absolute; left: 31px; top: 1128px; white-space: nowrap;
    font-weight: 300; font-size: 16px; letter-spacing: 3.2px;
  }
  .brand {
    position: absolute; left: 679px; top: 1109px; display: flex; align-items: center; gap: 10px;
  }
  .brand-mark { width: 58px; height: 58px; border-radius: 50%; background: var(--white); }
  .brand-name { font-weight: 400; font-size: 40px; letter-spacing: 1px; color: var(--white); }
</style>
</head>
<body>
<main class="flyer">
  <p class="address">4217 MARLOW AVENUE SACRAMENTO</p>

  <div class="photo-area" role="img" aria-label="Photo of a glowing pink and blue jellyfish drifting through dark water"></div>

  <svg class="neon-frames" width="960" height="1200" aria-hidden="true">
    <polygon class="frame-pink" points="297,483 540,573 462,785 206,725"/>
    <polygon class="frame-blue" points="337,470 554,614 398,822 192,686"/>
  </svg>

  <h1 class="lineup title">FRIDAYS</h1>
  <p class="lineup date">01.05.20</p>

  <p class="lineup floor-label floor-club">CLUB FLOOR</p>
  <p class="lineup dj dj-club">DJ VORTAN</p>

  <p class="lineup floor-label floor-lounge">LOUNGE FLOOR</p>
  <p class="lineup dj dj-lounge">DJ RUZO<br>DJ TAV</p>

  <p class="website">WWW.HARBORVENUEHALL.EXAMPLE FOR VIP INQUIRIES</p>

  <div class="brand">
    <span class="brand-mark"></span>
    <span class="brand-name">HARBOR</span>
  </div>
</main>
</body>
</html>
```